Medida Certa - Working hours register App needs interface design

Medida Certa, a 1 million users Brazilian website focused on general calculations needs an interface to an App for registering the working hours of a housemaid, a nanny, a housekeeper or other domestic workers.
The final users should be mainly housewifes.
The wireframe of the pages is in the LarPonto_layout.xls file attached.
Logo is also available in the wireframe.
The interface should be optimized for Android on Orbita KX with a 5'' screen.
Target Market(s)
Females, educated, from 30 to 50 y.o.
Industry/Entity Type
Android
Look and feel
Each slider illustrates characteristics of the customer's brand and the style your logo design should communicate.

```html
<!DOCTYPE html>
<html lang="en">
<head>
<meta charset="utf-8">
<title>Medida Certa - LarPonto</title>
<link href="https://fonts.googleapis.com/css2?family=Open+Sans:ital,wght@0,400;0,700;0,800;1,700&display=swap" rel="stylesheet">
<style>
:root{
  --teal:#5cc2b2;
  --teal-dark:#4fae9f;
  --header:#3f3f3f;
  --brand-red:#d62b27;
  --page:#ededed;
  --card:#ffffff;
  --line:#e2e2e2;
  --ink:#222222;
  --muted:#555555;
  --avatar:#c9b79d;
}
*{box-sizing:border-box;margin:0;padding:0}
html,body{width:670px;height:1200px;overflow:hidden;background:var(--page);font-family:"Open Sans",Arial,sans-serif}
.app{width:670px;height:1200px;position:relative;display:flex;flex-direction:column;background:var(--page)}
.app-header{height:112px;background:var(--header);display:flex;align-items:center;position:relative}
.brand{display:flex;align-items:center;padding-left:26px;flex:1}
.brand-mark{width:62px;height:62px;background:var(--brand-red);border-radius:6px;margin-right:20px}
.brand-name{color:#fff;font-weight:800;font-size:27px;letter-spacing:.5px}
.edit-button{width:102px;height:112px;background:var(--teal);display:flex;align-items:center;justify-content:center}
.section-title{font-weight:800;font-size:25px;color:var(--ink);padding:30px 0 14px 22px;letter-spacing:.3px}
.employee-list{list-style:none;margin:0 10px;background:var(--card);flex:1;overflow:hidden}
.employee{height:188px;display:flex;align-items:center;border-bottom:2px solid var(--line);padding:0 24px 0 12px}
.employee.is-selected{background:var(--teal)}
.avatar{width:160px;height:160px;border-radius:50%;border:6px solid #f3f3f3;background:radial-gradient(circle at 50% 40%,#e6d7c2 0,var(--avatar) 55%,#6f6a66 100%);flex:none}
.employee-name{flex:1;margin-left:34px;font-weight:700;font-style:italic;font-size:23px;color:var(--ink)}
.is-selected .employee-name{color:#fff}
.keyboard-icon{width:36px;height:24px;flex:none}
.bottom-nav{height:116px;background:var(--teal);display:flex}
.nav-item{flex:1;display:flex;flex-direction:column;align-items:center;justify-content:center;color:#fff;font-weight:700;font-size:15px;border-left:2px solid rgba(255,255,255,.55)}
.nav-item:first-child{border-left:none;background:var(--teal-dark)}
.nav-item svg{width:40px;height:40px;margin-bottom:10px}
</style>
</head>
<body>
<div class="app">
  <header class="app-header">
    <div class="brand">
      <span class="brand-mark"></span>
      <span class="brand-name">MEDIDA CERTA - LARPONTO</span>
    </div>
    <div class="edit-button" aria-label="Edit">
      <svg width="40" height="40" viewBox="0 0 24 24"><path fill="#fff" d="M3 17.2V21h3.8L17.8 10l-3.8-3.8L3 17.2zM20.7 7.1a1 1 0 0 0 0-1.4l-2.4-2.4a1 1 0 0 0-1.4 0L15 5.2 18.8 9l1.9-1.9z"/></svg>
    </div>
  </header>

  <h1 class="section-title">EMPLOYEE LIST</h1>

  <ul class="employee-list">
    <li class="employee"><div class="avatar" role="img" aria-label="Portrait photo of employee"></div><span class="employee-name">Beatriz Moura</span>
      <svg class="keyboard-icon" viewBox="0 0 36 24"><rect x="1" y="1" width="34" height="22" rx="2" fill="none" stroke="#444" stroke-width="2"/><g fill="#444"><rect x="5" y="5" width="4" height="3"/><rect x="11" y="5" width="4" height="3"/><rect x="17" y="5" width="4" height="3"/><rect x="23" y="5" width="4" height="3"/><rect x="5" y="10" width="4" height="3"/><rect x="11" y="10" width="4" height="3"/><rect x="17" y="10" width="4" height="3"/><rect x="23" y="10" width="8" height="3"/><rect x="9" y="16" width="18" height="3"/></g></svg></li>
    <li class="employee"><div class="avatar" role="img" aria-label="Portrait photo of employee"></div><span class="employee-name">Clara Lima</span>
      <svg class="keyboard-icon" viewBox="0 0 36 24"><rect x="1" y="1" width="34" height="22" rx="2" fill="none" stroke="#444" stroke-width="2"/><g fill="#444"><rect x="5" y="5" width="4" height="3"/><rect x="11" y="5" width="4" height="3"/><rect x="17" y="5" width="4" height="3"/><rect x="23" y="5" width="4" height="3"/><rect x="5" y="10" width="4" height="3"/><rect x="11" y="10" width="4" height="3"/><rect x="17" y="10" width="4" height="3"/><rect x="23" y="10" width="8" height="3"/><rect x="9" y="16" width="18" height="3"/></g></svg></li>
    <li class="employee is-selected"><div class="avatar" role="img" aria-label="Portrait photo of employee"></div><span class="employee-name">Daniela Rocha</span>
      <svg class="keyboard-icon" viewBox="0 0 36 24"><rect x="1" y="1" width="34" height="22" rx="2" fill="none" stroke="#fff" stroke-width="2"/><g fill="#fff"><rect x="5" y="5" width="4" height="3"/><rect x="11" y="5" width="4" height="3"/><rect x="17" y="5" width="4" height="3"/><rect x="23" y="5" width="4" height="3"/><rect x="5" y="10" width="4" height="3"/><rect x="11" y="10" width="4" height="3"/><rect x="17" y="10" width="4" height="3"/><rect x="23" y="10" width="8" height="3"/><rect x="9" y="16" width="18" height="3"/></g></svg></li>
    <li class="employee"><div class="avatar" role="img" aria-label="Portrait photo of employee"></div><span class="employee-name">Elisa Ramos</span>
      <svg class="keyboard-icon" viewBox="0 0 36 24"><rect x="1" y="1" width="34" height="22" rx="2" fill="none" stroke="#444" stroke-width="2"/><g fill="#444"><rect x="5" y="5" width="4" height="3"/><rect x="11" y="5" width="4" height="3"/><rect x="17" y="5" width="4" height="3"/><rect x="23" y="5" width="4" height="3"/><rect x="5" y="10" width="4" height="3"/><rect x="11" y="10" width="4" height="3"/><rect x="17" y="10" width="4" height="3"/><rect x="23" y="10" width="8" height="3"/><rect x="9" y="16" width="18" height="3"/></g></svg></li>
    <li class="employee"><div class="avatar" role="img" aria-label="Portrait photo of employee"></div></li>
  </ul>

  <nav class="bottom-nav">
    <div class="nav-item">
      <svg viewBox="0 0 24 24" fill="#fff"><rect x="2" y="4" width="3" height="3"/><rect x="7" y="4" width="15" height="3"/><rect x="2" y="10.5" width="3" height="3"/><rect x="7" y="10.5" width="15" height="3"/><rect x="2" y="17" width="3" height="3"/><rect x="7" y="17" width="15" height="3"/></svg>
      EMPLOYEE LIST</div>
    <div class="nav-item">
      <svg viewBox="0 0 24 24"><circle cx="10" cy="10" r="6.5" fill="none" stroke="#fff" stroke-width="2.6"/><path d="M15 15l6 6" stroke="#fff" stroke-width="3.2" stroke-linecap="round"/></svg>
      SEARCH</div>
    <div class="nav-item">
      <svg viewBox="0 0 24 24" fill="#fff"><circle cx="14" cy="7" r="4.5"/><path d="M5 22c0-5 4-8.5 9-8.5s9 3.5 9 8.5z"/><rect x="1" y="7" width="8" height="2.4"/><rect x="3.8" y="4.2" width="2.4" height="8"/></svg>
      ADD</div>
    <div class="nav-item">
      <svg viewBox="0 0 24 24" fill="none" stroke="#fff" stroke-width="2.6" stroke-linecap="round"><path d="M7 6.5a8 8 0 1 0 10 0"/><path d="M12 2.5v9"/></svg>
      EXIT</div>
  </nav>
</div>
</body>
</html>
```